Marine & Offshore company business card

We need a new logo design for a new company based in Singapore called "Vontique Global Pte. Ltd.". We are suppliers of electrical items to marine and offshore industry. We specialise in lightings, cables terminations and junction box customisation. We would like the name card to have simple modern classic look.

Target Market(s)

my target customers are ship owners, shipyard purchasers, offshore purchasers.

Industry/Entity Type

Electrical

Font styles to use
Serif
Sans Serif

Colors

Designer to choose colors to be used in the design.

```html
<!DOCTYPE html>
<html lang="en">
<head>
<meta charset="utf-8">
<title>Vontique Global Pte. Ltd. – Business Card</title>
<link rel="stylesheet" href="https://fonts.googleapis.com/css2?family=Marcellus&family=Cormorant+Garamond:wght@500&family=Montserrat:wght@500&display=swap">
<style>
  :root {
    --page: #e9e7e3;
    --card-white: #ffffff;
    --marine-blue: #0d4a93;
    --steel-grey: #7d7f83;
    --navy-ink: #1c2b44;
    --brass: #c99a2e;
    --on-blue: #ffffff;
  }
  * { box-sizing: border-box; margin: 0; padding: 0; }
  html, body { width: 1200px; height: 1000px; overflow: hidden; }
  body {
    background: var(--page);
    position: relative;
    font-family: "Montserrat", sans-serif;
  }
  .card {
    position: absolute;
    left: 300px;
    width: 600px;
    height: 343px;
    border-radius: 28px;
    overflow: hidden;
    box-shadow: 0 6px 18px rgba(0,0,0,0.18);
  }
  .card--front { top: 110px; background: var(--card-white); }
  .card--back  { top: 547px; background: var(--marine-blue); }

  .card__waves { position: absolute; inset: 0; width: 600px; height: 343px; }

  .wordmark {
    position: absolute;
    display: flex;
    align-items: center;
    gap: 10px;
    font-family: "Marcellus", serif;
    letter-spacing: 1px;
    white-space: nowrap;
  }
  .wordmark__dot {
    border-radius: 50%;
    background: var(--brass);
    flex: none;
  }
  .card--front .wordmark { left: 62px; top: 120px; font-size: 18px; color: var(--navy-ink); }
  .card--front .wordmark__dot { width: 20px; height: 20px; }
  .card--back .wordmark  { left: 50%; top: 50%; transform: translate(-50%, -50%); font-size: 26px; color: var(--on-blue); }
  .card--back .wordmark__dot { width: 26px; height: 26px; background: var(--on-blue); }

  .contact {
    position: absolute;
    right: 28px;
    top: 118px;
    text-align: right;
    color: var(--on-blue);
    font-size: 13px;
    line-height: 21px;
    list-style: none;
  }
  .contact__gap { margin-top: 6px; }

  .holder {
    position: absolute;
    left: 44px;
    bottom: 30px;
    color: var(--on-blue);
    font-family: "Cormorant Garamond", serif;
    font-weight: 500;
  }
  .holder__name { font-size: 24px; letter-spacing: 1px; line-height: 1; }
  .holder__role { font-size: 17px; margin-left: 62px; line-height: 1.1; }
</style>
</head>
<body>

<section class="card card--front" aria-label="Business card front">
  <svg class="card__waves" viewBox="0 0 600 343" aria-hidden="true">
    <path d="M450 0 C430 150 240 232 0 244 L0 343 L600 343 L600 0 Z" fill="var(--steel-grey)"/>
    <path d="M464 0 C444 150 254 236 0 254 L0 343 L600 343 L600 0 Z" fill="var(--card-white)"/>
    <path d="M472 0 C452 152 262 240 0 262 L0 343 L600 343 L600 0 Z" fill="var(--marine-blue)"/>
  </svg>

  <div class="wordmark"><span class="wordmark__dot"></span><span class="wordmark__name">VONTIQUE GLOBAL PTE. LTD.</span></div>

  <ul class="contact">
    <li>0000 Harbour Point</li>
    <li>Singapore</li>
    <li class="contact__gap">000-000-0000</li>
    <li>hello@vontique.com</li>
    <li>www.vontiqueglobal.com</li>
  </ul>

  <div class="holder">
    <p class="holder__name">YOUR NAME</p>
    <p class="holder__role">Director</p>
  </div>
</section>

<section class="card card--back" aria-label="Business card back">
  <div class="wordmark"><span class="wordmark__dot"></span><span class="wordmark__name">VONTIQUE GLOBAL PTE. LTD.</span></div>
</section>

</body>
</html>
```